Lift Your Standing - Search Engine Website

I am launching an SEO website and I am looking to have the site designed. There are a total of 8-10 pages that will need to be designed. I am providing 2 pages off the bat and will work with a designer once these 2 pages are complete. I have never posted a contest for website design (only logos, brochures, etc) so please let me know if there is anything you need from me. I am uploading 2 versions of our logo - a horizontal and a vertical version. I was thinking of getting these rendered in 3d, but I am just going with these for now. I am hoping to complete all work in 10 days, so hopefully the right design for the 1st 2 pages are submitted promptly.

We provide search engine optomization tools and backlinking tools. We provide free research tools as well as cost effective packages for SEO.

I am including 2 word files that have info about the home page and keyword summary page. Additional pages will include: Keyword Research Summary, The Slate, Reports, etc.

I am also uploading a zip file that has some examples of home pages that I like. None of them are exactly what I am looking for, but they have certain elements that I like.

I am looking for a clean design and stands out and has good use of color.

Link to instructions files (2...more will be uploaded as first 2 pages are finalized): https://www.filecrate-example.net/sh/k4m2w7z9q3v1b8x/tRn_p-7ab2
Updates

Forgot to include our logos. Here is a drop box link to the logos: 

https://www.filecrate-example.net/sh/93jd2kq7zt5wmvp/8h2PLmz4Xe

Target Market(s)

big and small businesses, resellers

Industry/Entity Type

Seo

Requirements
Must have
• see attached MS Word files for details about requirements.

```html
<!DOCTYPE html>
<html lang="en">
<head>
<meta charset="utf-8">
<title>Lift Your Standing – Search Engine Rankings</title>
<link rel="stylesheet" href="https://fonts.googleapis.com/css2?family=Roboto+Condensed:wght@400;700&family=Open+Sans:ital,wght@1,400&display=swap">
<style>
:root{
  --navy:#1f3b63;
  --sky:#27b0ec;
  --blue-deep:#0b6fcf;
  --blue-light:#3fc2f5;
  --orange:#ffb400;
  --orange-dark:#f39a00;
  --green:#8dcf1c;
  --green-dark:#5fae0c;
  --grey-bg:#efefef;
  --grey-text:#9a9a9a;
  --ink:#444;
  --ink-icon:#4a4a4a;
  --white:#fff;
  --black:#0b0b0b;
}
*{box-sizing:border-box;margin:0;padding:0}
html,body{width:870px;height:1200px;overflow:hidden}
body{position:relative;background:var(--grey-bg);font-family:"Roboto Condensed",Arial,sans-serif;color:var(--ink)}
.abs{position:absolute}

/* header */
.site-header{top:0;left:0;width:870px;height:57px;background:var(--white);box-shadow:0 2px 4px rgba(0,0,0,.15);z-index:2}
.brand{left:75px;top:19px;font-size:21px;font-weight:700;color:var(--blue-deep);letter-spacing:-.3px}
.main-nav{right:76px;top:24px;display:flex;gap:0;list-style:none;font-size:11.5px;font-weight:700;color:var(--navy)}
.main-nav li{padding:3px 8px;line-height:14px}
.main-nav .active{background:var(--sky);color:var(--white)}
.main-nav .login{background:var(--orange);color:var(--white);margin-left:5px;padding:3px 4px}

/* hero */
.hero{top:57px;left:0;width:870px;height:285px;background:linear-gradient(120deg,#0a5fc4 0%,#1d8ee6 45%,#45c6f6 75%,#1f8fe2 100%);overflow:hidden}
.hero svg.waves{position:absolute;left:0;top:0}
.hero-title{left:75px;top:58px;width:490px;font-size:31px;line-height:41px;font-weight:700;color:var(--white);text-shadow:0 1px 2px rgba(0,0,0,.25)}
.btn{display:flex;align-items:center;justify-content:center;color:var(--white);font-weight:700;text-transform:uppercase;box-shadow:0 3px 5px rgba(0,0,0,.3)}
.btn-buy{left:74px;top:205px;width:131px;height:33px;font-size:17px;background:linear-gradient(var(--orange),var(--orange-dark))}
.btn-trial{left:215px;top:205px;width:131px;height:33px;font-size:17px;background:linear-gradient(var(--green),var(--green-dark))}
.share-note{left:432px;top:200px;transform:rotate(-20deg);transform-origin:left top;font-family:"Open Sans",sans-serif;font-style:italic;font-size:13px;line-height:15px;color:var(--white);text-align:center}

/* research card */
.research{left:563px;top:72px;width:232px;height:249px;background:var(--white);box-shadow:0 2px 6px rgba(0,0,0,.3);z-index:3}
.research-head{height:61px;background:linear-gradient(#ffc21a,var(--orange-dark));color:var(--white);font-size:25px;padding:20px 0 0 65px}
.research-head .lens{position:absolute;left:22px;top:-6px;width:44px;height:44px;border-radius:50%;background:radial-gradient(#fff6d0,#e3b54a)}
.field{position:absolute;left:10px;width:205px;height:26px;border:1px solid #dcdcdc;border-radius:13px;font-family:"Open Sans",sans-serif;font-style:italic;font-size:10px;color:#b8b8b8;padding:6px 14px}
.field svg{position:absolute;right:9px;top:5px}
.btn-signup{left:54px;top:224px;width:130px;height:32px;font-size:17px;background:linear-gradient(#ffc21a,var(--orange-dark))}

/* social row */
.touch-label{left:75px;top:397px;font-size:13px;font-weight:700;color:var(--navy)}
.social-tile{top:378px;width:45px;height:45px;border-radius:7px;box-shadow:0 2px 3px rgba(0,0,0,.3)}

/* blog */
.blog{left:75px;top:443px;width:474px;height:162px;background:var(--white);box-shadow:0 1px 3px rgba(0,0,0,.2)}
.blog-illus{left:18px;top:-8px;width:72px;height:62px;border-radius:5px;background:linear-gradient(#e9c08a,#c48a4c)}
.blog-title{left:102px;top:18px;font-size:27px;color:#555}
.post{top:70px;width:210px}
.post h3{font-size:13.5px;font-weight:400;color:#444;margin-bottom:6px}
.post p{font-family:"Open Sans",sans-serif;font-style:italic;font-size:10.5px;line-height:18px;color:var(--grey-text)}
.read-more{display:inline-block;margin-top:8px;background:var(--sky);color:var(--white);font-size:7px;font-weight:700;padding:3px 4px}

/* side */
.video{left:564px;top:379px;width:231px;height:152px;background:linear-gradient(135deg,#c9ced2,#8d9499 60%,#5b6166)}
.video-bar{left:0;bottom:0;width:231px;height:22px;background:#1b1b1b}
.invite{left:564px;top:544px;width:230px;height:61px;background:linear-gradient(#2d95e6,#0b61bd);color:var(--white);text-align:center;padding-left:40px}
.invite .small{font-size:13px;padding-top:6px}
.invite .big{font-size:27px;font-weight:700;line-height:28px}
.invite .dot{position:absolute;left:8px;top:10px;width:26px;height:26px;border-radius:50%;background:rgba(255,255,255,.25)}

/* features */
.feature{width:225px}
.feature .icon{position:absolute;left:0;top:0;width:45px;height:40px}
.feature h4{margin-left:54px;font-size:15px;font-weight:700;line-height:18px;color:#4d4d4d;min-height:36px;display:flex;align-items:center}
.feature p{margin-top:11px;font-family:"Open Sans",sans-serif;font-style:italic;font-size:10.5px;line-height:18px;color:#b4b4b4}

/* footer */
.site-footer{left:0;top:1027px;width:870px;height:173px;background:var(--black);color:var(--white)}
.foot-col h5{font-size:14px;font-weight:400;margin-bottom:10px}
.foot-col ul{list-style:none;font-size:10.5px}
.foot-col li{height:23.5px;padding-left:17px;position:relative}
.foot-col li::before{content:"";position:absolute;left:0;top:3px;border-left:6px solid var(--white);border-top:4px solid transparent;border-bottom:4px solid transparent}
.foot-col .social li{padding-left:24px;height:29px;padding-top:3px}
.foot-col .social li::before{border:1.5px solid var(--white);border-radius:50%;width:16px;height:16px;top:0}
.foot-rule{left:75px;top:137px;width:720px;border-top:1px solid #2a2a2a}
.copyright{left:75px;top:148px;font-size:10.5px}
</style>
</head>
<body>

<header class="site-header abs">
  <div class="brand abs">LiftYourStanding.net</div>
  <ul class="main-nav abs">
    <li>ABOUT US</li><li>SERVICES</li><li class="active">FEATURES</li><li>RESOURCES</li><li>FREE TRIAL</li><li>FAQ</li><li>CONTACT</li><li class="login">LOG IN</li>
  </ul>
</header>

<section class="hero abs">
  <svg class="waves" width="870" height="285" viewBox="0 0 870 285">
    <path d="M0 160 Q300 60 870 140 L870 0 L0 0Z" fill="rgba(255,255,255,.06)"/>
    <path d="M0 285 L0 190 Q180 240 260 285Z" fill="rgba(0,40,120,.25)"/>
    <path d="M600 285 Q720 200 870 170 L870 285Z" fill="rgba(255,255,255,.1)"/>
  </svg>
  <h1 class="hero-title abs">Boost Your Search Engine Rankings Using Legal Back Linking Techniques</h1>
  <div class="btn btn-buy abs">Buy Now</div>
  <div class="btn btn-trial abs">Free Trial</div>
  <div class="share-note abs">Share this on<br>Circlebook</div>
  <svg class="abs" style="left:494px;top:228px" width="54" height="22" viewBox="0 0 54 22"><path d="M3 4 Q20 20 48 12" fill="none" stroke="#fff" stroke-width="3" stroke-linecap="round"/><path d="M40 6 L50 12 L41 18" fill="none" stroke="#fff" stroke-width="3" stroke-linecap="round"/></svg>
</section>

<aside class="research abs">
  <div class="research-head abs" style="left:0;top:0;width:232px"><span class="lens" role="img" aria-label="Magnifying glass illustration"></span>Free Research</div>
  <div class="field" style="top:78px">Enter Your URL<svg width="16" height="16" viewBox="0 0 16 16"><circle cx="6" cy="6" r="4.5" fill="none" stroke="#bbb" stroke-width="2"/><path d="M9.5 9.5 L14 14" stroke="#bbb" stroke-width="3"/></svg></div>
  <div class="field" style="top:124px">Enter Your Keywords Here<svg width="16" height="16" viewBox="0 0 16 16"><circle cx="6" cy="6" r="4.5" fill="none" stroke="#bbb" stroke-width="2"/><path d="M9.5 9.5 L14 14" stroke="#bbb" stroke-width="3"/></svg></div>
  <div class="field" style="top:169px">Type In Competitor URL Here<svg width="16" height="16" viewBox="0 0 16 16"><circle cx="6" cy="6" r="4.5" fill="none" stroke="#bbb" stroke-width="2"/><path d="M9.5 9.5 L14 14" stroke="#bbb" stroke-width="3"/></svg></div>
  <div class="btn btn-signup abs">Sign Up</div>
</aside>

<div class="touch-label abs">GET IN TOUCH WITH US</div>
<div class="social-tile abs" style="left:220px;background:linear-gradient(#5b8fd6,#2c5cae)"></div>
<div class="social-tile abs" style="left:271px;background:linear-gradient(#6fd4f4,#22a3d8)"></div>
<div class="social-tile abs" style="left:326px;background:linear-gradient(#ffc64a,#f08c00)"></div>

<section class="blog abs">
  <div class="blog-illus abs" role="img" aria-label="Notepad and pencil illustration"></div>
  <h2 class="blog-title abs">Latest Blog Posts</h2>
  <article class="post abs" style="left:21px">
    <h3>Native Advertising</h3>
    <p>Vestibulum feugiat magna in mi tincidunt a blandit dui mollis. leo.</p>
    <span class="read-more">READ MORE</span>
  </article>
  <article class="post abs" style="left:244px">
    <h3>Teething Pains</h3>
    <p>Vestibulum feugiat magna in mi tincidunt a blandit dui mollis.</p>
    <span class="read-more">READ MORE</span>
  </article>
</section>

<div class="video abs" role="img" aria-label="Promotional video still of two smiling business people in an office">
  <svg class="abs" style="left:95px;top:44px" width="50" height="50" viewBox="0 0 50 50"><circle cx="25" cy="25" r="24" fill="rgba(255,255,255,.7)"/><path d="M19 14 L37 25 L19 36Z" fill="#fff"/></svg>
  <div class="video-bar abs"><svg width="231" height="22" viewBox="0 0 231 22"><path d="M10 7 L16 11 L10 15Z" fill="#fff"/><rect x="33" y="9" width="140" height="4" fill="#555"/><rect x="33" y="9" width="45" height="4" fill="#2a9ce0"/></svg></div>
</div>

<div class="invite abs"><span class="dot"></span><div class="small">Invite Your Friends via</div><div class="big">CIRCLEBOOK</div></div>

<!-- features grid -->
<div class="feature abs" style="left:75px;top:656px">
  <svg class="icon" viewBox="0 0 45 40"><rect x="3" y="10" width="6" height="22" fill="var(--ink-icon)"/><rect x="11" y="2" width="6" height="30" fill="var(--ink-icon)"/><rect x="19" y="8" width="6" height="24" fill="var(--ink-icon)"/><rect x="27" y="14" width="6" height="18" fill="var(--ink-icon)"/><rect x="0" y="33" width="42" height="2" fill="var(--ink-icon)"/></svg>
  <h4>Why Lift Your<br>Standing?</h4>
  <p>Vestibulum feugiat magna in mi tincidunt a blandit dui mollis.</p>
</div>
<div class="feature abs" style="left:312px;top:656px">
  <svg class="icon" viewBox="0 0 45 40"><path d="M13 8 L13 2 L29 2 L29 8" fill="none" stroke="var(--ink-icon)" stroke-width="2"/><rect x="1" y="8" width="40" height="26" fill="none" stroke="var(--ink-icon)" stroke-width="3"/><text x="21" y="28" text-anchor="middle" font-family="Roboto Condensed,sans-serif" font-weight="700" font-size="13" fill="var(--ink-icon)">sale</text></svg>
  <h4>Free Trial</h4>
  <p>Vestibulum feugiat magna in mi tincidunt a blandit dui mollis.</p>
</div>
<div class="feature abs" style="left:556px;top:656px;width:235px">
  <svg class="icon" viewBox="0 0 45 40"><rect x="3" y="10" width="6" height="22" fill="var(--ink-icon)"/><rect x="11" y="2" width="6" height="30" fill="var(--ink-icon)"/><rect x="19" y="8" width="6" height="24" fill="var(--ink-icon)"/><rect x="27" y="14" width="6" height="18" fill="var(--ink-icon)"/><rect x="0" y="33" width="42" height="2" fill="var(--ink-icon)"/></svg>
  <h4>SEO Basics</h4>
  <p>Vestibulum feugiat magna in mi tincidunt a blan-dit dui mollis.</p>
</div>

<div class="feature abs" style="left:75px;top:778px">
  <svg class="icon" viewBox="0 0 45 40"><rect x="8" y="4" width="26" height="20" fill="none" stroke="var(--ink-icon)" stroke-width="2"/><rect x="11" y="7" width="20" height="14" fill="var(--ink-icon)"/><rect x="18" y="24" width="6" height="6" fill="var(--ink-icon)"/><rect x="12" y="30" width="18" height="3" fill="var(--ink-icon)"/></svg>
  <h4>Tips To Using Our<br>System</h4>
  <p>Vestibulum feugiat magna in mi tincidunt a blandit dui mollis.</p>
</div>
<div class="feature abs" style="left:312px;top:778px">
  <svg class="icon" viewBox="0 0 45 40"><rect x="2" y="6" width="19" height="24" fill="none" stroke="var(--ink-icon)" stroke-width="2"/><rect x="21" y="6" width="19" height="24" fill="none" stroke="var(--ink-icon)" stroke-width="2"/><path d="M6 12h11M6 17h11M6 22h11M25 12h11M25 17h11M25 22h11" stroke="var(--ink-icon)" stroke-width="1.5"/></svg>
  <h4>SEO Tips</h4>
  <p>Vestibulum feugiat magna in mi tincidunt a blandit dui mollis.</p>
</div>
<div class="feature abs" style="left:556px;top:778px;width:235px">
  <svg class="icon" viewBox="0 0 45 40"><circle cx="10" cy="22" r="8" fill="none" stroke="var(--ink-icon)" stroke-width="2"/><circle cx="34" cy="22" r="8" fill="none" stroke="var(--ink-icon)" stroke-width="2"/><path d="M18 20 Q22 16 26 20 M2 20 L8 10 M42 20 L36 10" fill="none" stroke="var(--ink-icon)" stroke-width="2"/></svg>
  <h4>Free Keyword<br>Analysis Tools</h4>
  <p>Vestibulum feugiat magna in mi tincidunt a blan-dit dui mollis.</p>
</div>

<div class="feature abs" style="left:75px;top:899px">
  <svg class="icon" viewBox="0 0 45 40"><rect x="10" y="4" width="2.5" height="30" fill="var(--ink-icon)"/><path d="M12 5 Q22 2 34 6 L34 22 Q22 18 12 21Z" fill="var(--ink-icon)"/></svg>
  <h4>What To<br>Expect</h4>
  <p>Vestibulum feugiat magna in mi tincidunt a blandit dui mollis.</p>
</div>
<div class="feature abs" style="left:312px;top:899px">
  <svg class="icon" viewBox="0 0 45 40"><path d="M24 4 L38 4 L38 18 L18 38 L4 24Z" fill="var(--ink-icon)"/><circle cx="32" cy="10" r="2.5" fill="var(--grey-bg)"/><text x="20" y="27" text-anchor="middle" font-family="Roboto Condensed,sans-serif" font-weight="700" font-size="12" fill="var(--grey-bg)" transform="rotate(-45 20 23)">%</text></svg>
  <h4>White Label</h4>
  <p>Vestibulum feugiat magna in mi tincidunt a blandit dui mollis.</p>
</div>
<div class="feature abs" style="left:556px;top:899px;width:235px">
  <svg class="icon" viewBox="0 0 45 40"><path d="M20 2 L25 14 L38 14 L28 22 L32 35 L20 27 L8 35 L12 22 L2 14 L15 14Z" fill="var(--ink-icon)"/></svg>
  <h4>Pre Lift<br>Checklist</h4>
  <p>Vestibulum feugiat magna in mi tincidunt a blan-dit dui mollis.</p>
</div>

<footer class="site-footer abs">
  <div class="foot-col abs" style="left:75px;top:15px">
    <h5>Company</h5>
    <ul><li>About Us</li><li>Why Lift Your Standing</li><li>FAQ</li><li>Affiliate Program</li></ul>
  </div>
  <div class="foot-col abs" style="left:223px;top:39px">
    <ul><li>Tips To Using Our System</li><li>Contact us</li><li>Terms of Use</li><li>Privacy Policy</li></ul>
  </div>
  <div class="foot-col abs" style="left:385px;top:15px">
    <h5>Services</h5>
    <ul><li>Link Building</li><li>Local SEO</li><li>Free Trial</li><li>Free Keyword Analysis Tools</li></ul>
  </div>
  <div class="foot-col abs" style="left:555px;top:15px">
    <h5>SEO</h5>
    <ul><li>SEO Basics</li><li>SEO Tips</li><li>On Page SEO</li><li>Off Page SEO</li></ul>
  </div>
  <div class="foot-col abs" style="left:671px;top:15px">
    <h5>Get in Touch</h5>
    <ul class="social"><li>Circlebook</li><li>Chirper</li></ul>
  </div>
  <div class="foot-rule abs"></div>
  <div class="copyright abs">Lifting Your Standing 2013 Copyright! All rights Reserved!</div>
</footer>

</body>
</html>
```